Modern, Clean website for painting service.

We are working with a company called Brushwell Crafts and building a new website for them.

Some sites to use for content/competitors and inspiration:

https://www.coatvantaged.com
https://ridgeline-hue.com
https://tedvarnokcoating.com

Thank you for taking the time to consider designing a website for us. We are web developers based in Stockton, CA, USA. Most of our projects go through the same process. Understanding this process may help you win a project with us. We custom-code all of our websites in-house. We don’t have any requirements as to what tools you use for your design, but we prefer Figma files. For any design that we label as four-stars, we send it to the client for review. The client picks the final design they want us to use. Once we complete this process, we will continue to show additional clients all the four-star sites and purchase them later. Your designs will have multiple chances to sell. For better chances of success, we ask that you follow these guidelines.

IMAGES:
If you use any images or icons in the design, we ask that you have a link to the asset so we can purchase the image/icon. Most of the designs we submit do not have the customer’s images on them unless they have some great images. Be creative; show us the feeling you are trying to portray with your image choices. Use any royalty-free site you choose. We subscribe to Kelvra and mainly use their images, but we can purchase images outside of Kelvra. PLEASE NOTE: we will not submit designs to clients with watermarks on the images.

FONTS:
We ask that you identify the fonts used in the design. This can be done in a message if you want. We typically use Google Fonts and Kelvra Type.

CONTENT:
We're always open to different content and ideas. We often submit designs with stock images so the client can see our vision. We typically take pictures after the website launch to use their images with our vision. Lorem Ipsum is fine for paragraphs, but we ask that you write the headers in correct English. We want to be able to show the vision and identify the sections of the website.

INSPIRATION:
We typically add a couple of links in the brief of websites we like to help you get started in your design.

REVISIONS:
We do not often ask for revisions of the designs unless we see something in the design that may not appeal to the client. If there are slight changes that we want to make, we do that in the development process.

FEEDBACK:
We rarely give feedback on designs during the design process. We are working on many website projects and do not have the time to provide feedback. We usually respond if your request is well thought out and asks specific questions, but a note asking “feedback, please” usually goes unanswered.

```html
<!DOCTYPE html>
<html lang="en">
<head>
<meta charset="utf-8">
<title>Brushwell Crafts – House Painting Services</title>
<link rel="stylesheet" href="https://fonts.googleapis.com/css2?family=Jost:wght@400;500;600&family=Montserrat:wght@400;600&display=swap">
<style>
:root{
  --navy:#071e48;
  --crimson:#8a0a1f;
  --ink:#111111;
  --body:#3a3a3a;
  --light:#f4f4f4;
  --white:#ffffff;
  --field:#ffffff;
}
*{box-sizing:border-box;margin:0;padding:0}
html,body{width:1200px;height:4147px;overflow:hidden}
body{position:relative;font-family:'Jost',sans-serif;color:var(--ink);background:var(--white)}
.abs{position:absolute}
/* header */
.site-header{left:0;top:0;width:1200px;height:90px;background:var(--white)}
.brand{left:42px;top:34px;display:flex;align-items:center;gap:8px;font-size:14px;font-weight:500;color:var(--navy);letter-spacing:.5px;white-space:nowrap}
.brand-mark{width:14px;height:14px;background:var(--crimson)}
.main-nav{left:255px;top:32px;display:flex;gap:42px;font-size:18px;letter-spacing:4px;color:var(--ink)}
.header-phone{left:832px;top:30px;display:flex;align-items:center;gap:6px;font-size:18px;font-weight:500;color:var(--ink)}
.btn{display:flex;align-items:center;justify-content:center;background:var(--navy);color:var(--white);letter-spacing:4px;font-size:17px;font-weight:500}
.header-cta{left:1022px;top:20px;width:143px;height:45px}
/* hero */
.hero{left:0;top:90px;width:1200px;height:620px;background:linear-gradient(180deg,#8c8270 0%,#b7ab97 35%,#d9d2c6 65%,#a99d8a 100%)}
.hero-title{left:0;top:275px;width:1200px;text-align:center;font-size:72px;font-weight:500;color:var(--white);line-height:1}
.hero-text{left:230px;top:381px;width:740px;text-align:center;font-size:19px;line-height:26px;color:var(--white)}
.hero-cta{left:488px;top:463px;width:228px;height:44px}
/* who we are */
.about{left:0;top:710px;width:1200px;height:450px;background:var(--light)}
.section-title{font-size:58px;font-weight:500;color:var(--ink);text-align:center;line-height:1}
.about-title{left:0;top:765px;width:1200px}
.about-text{left:240px;top:836px;width:720px;text-align:center;font-size:22px;line-height:37.5px;color:var(--body)}
.about-cta{left:493px;top:1062px;width:229px;height:44px}
/* services */
.service-photo{width:585px;height:510px}
.photo-house{left:0;top:1160px;background:linear-gradient(180deg,#8fb8e6 0%,#c5d6e6 30%,#6b6670 55%,#d5d1ca 80%,#b7b4ad 100%)}
.photo-building{left:585px;top:1670px;width:615px;height:508px;background:linear-gradient(160deg,#eef0f2 0%,#3f66b8 40%,#2f55a5 62%,#d9d9d9 82%,#b9b9b9 100%)}
.service-block{width:520px}
.service-title{font-size:54px;font-weight:600;line-height:62px;color:var(--ink)}
.service-lead{margin-top:14px;font-size:20px;color:var(--body)}
.service-list{list-style:none;margin-top:22px}
.service-list li{display:flex;align-items:center;gap:16px;height:50px;font-size:20px;font-weight:500;color:#222}
.residential{left:670px;top:1207px}
.commercial{left:88px;top:1725px}
/* reviews */
.reviews{left:0;top:2178px;width:1200px;height:485px;background:var(--navy)}
.reviews-title{left:0;top:2252px;width:1200px;color:var(--white);font-size:52px}
.review{width:440px;color:var(--white)}
.review-1{left:152px;top:2363px}
.review-2{left:645px;top:2363px}
.stars{display:flex;gap:10px}
.review-text{margin-top:26px;font-family:'Montserrat',sans-serif;font-size:23px;line-height:35px}
.review-name{margin-top:20px;margin-left:8px;font-family:'Montserrat',sans-serif;font-size:15px;font-weight:600}
/* results */
.results-title{left:0;top:2766px;width:1200px}
.result{top:2896px;width:270px;height:229px}
.result-1{left:145px;background:linear-gradient(90deg,#3b342d 0%,#6e4a32 40%,#e9e8e4 70%,#c9c7c2 100%)}
.result-2{left:455px;background:linear-gradient(90deg,#f3f5f7 0%,#2d8fb5 25%,#e5e9ec 50%,#7e8f9e 80%,#eef1f3 100%)}
.result-3{left:765px;background:linear-gradient(180deg,#8a8580 0%,#c8c4bc 45%,#a9a49c 70%,#7a4e2c 100%)}
.slider-arrow{top:2992px;font-size:40px;color:var(--ink)}
/* quote */
.quote{left:0;top:3240px;width:1200px;height:517px;background:var(--light)}
.quote-title{left:0;top:3305px;width:1200px}
.field{background:var(--field);border-radius:4px;font-family:'Montserrat',sans-serif;font-size:14px;color:#555;padding:11px 18px}
.quote-submit{left:266px;top:3620px;width:666px;height:50px;background:var(--crimson);color:var(--white);font-family:'Montserrat',sans-serif;font-size:15px;font-weight:600;display:flex;align-items:center;justify-content:center}
/* footer */
.site-footer{left:0;top:3757px;width:1200px;height:390px;background:var(--navy);color:var(--white)}
.footer-brand{left:80px;top:3870px;display:flex;align-items:center;gap:8px;font-size:18px;font-weight:500;letter-spacing:1px;color:var(--white);white-space:nowrap}
.footer-about{left:85px;top:3942px;width:280px;font-size:10px;line-height:13px;color:#d7dbe4}
.socials{left:85px;top:4012px;display:flex;gap:30px}
.social-dot{width:16px;height:16px;border-radius:50%;background:var(--white)}
.footer-heading{font-size:19px;font-weight:400;letter-spacing:.5px}
.quick-links{left:445px;top:3843px;color:var(--white)}
.quick-links ul{list-style:none;margin-top:22px;margin-left:12px}
.quick-links li{font-family:'Montserrat',sans-serif;font-size:13px;height:39px;display:flex;align-items:center;gap:8px}
.quick-links li::before{content:"";width:5px;height:5px;border-radius:50%;background:var(--crimson)}
.contact-info{left:680px;top:3840px;color:var(--white)}
.contact-row{display:flex;align-items:center;gap:10px;margin-top:22px;font-family:'Montserrat',sans-serif}
.contact-icon{width:22px;height:22px;border-radius:50%;background:var(--crimson);display:flex;align-items:center;justify-content:center}
.contact-label{font-size:9px;font-weight:600;letter-spacing:.3px}
.contact-value{font-size:13px;white-space:nowrap}
.stay-updated{left:935px;top:3840px;color:var(--white)}
.newsletter-input{margin-top:20px;width:156px;height:31px;background:var(--white);color:#888;font-family:'Montserrat',sans-serif;font-size:10px;display:flex;align-items:center;justify-content:center}
.newsletter-btn{margin-top:20px;width:156px;height:30px;background:var(--crimson);font-family:'Montserrat',sans-serif;font-size:12px;font-weight:600;display:flex;align-items:center;justify-content:center}
.copyright{left:88px;top:4105px;font-size:11px;color:var(--white)}
.legal{left:910px;top:4108px;font-size:10px;color:var(--white)}
</style>
</head>
<body>

<header class="site-header abs">
  <div class="brand abs"><span class="brand-mark"></span>BRUSHWELL CRAFTS</div>
  <nav class="main-nav abs"><span>HOME</span><span>ABOUT</span><span>SERVICES</span><span>PORTFOLIO</span></nav>
  <div class="header-phone abs">
    <svg width="24" height="24" viewBox="0 0 24 24"><path d="M6.6 10.8a15 15 0 0 0 6.6 6.6l2.2-2.2a1 1 0 0 1 1-.25 11.4 11.4 0 0 0 3.6.57 1 1 0 0 1 1 1V20a1 1 0 0 1-1 1A17 17 0 0 1 3 4a1 1 0 0 1 1-1h3.5a1 1 0 0 1 1 1c0 1.25.2 2.45.57 3.57a1 1 0 0 1-.25 1z" fill="#8a0a1f"/></svg>
    555-014-2290
  </div>
  <div class="btn header-cta abs">CONTACT</div>
</header>

<section class="hero abs" role="img" aria-label="Bright living room with staircase, white sofas and framed walls"></section>
<h1 class="hero-title abs">House Painting Services</h1>
<p class="hero-text abs">Lorem ipsum dolor sit amet, consectetur adipiscing elit, sed do eiusmod tempor incididunt ut labore et dolore magna aliqua. Ut enim ad minim veniam</p>
<div class="btn hero-cta abs">GET A QUOTE</div>

<section class="about abs"></section>
<h2 class="section-title about-title abs">Who We Are</h2>
<p class="about-text abs">Com uma rede consolidada de escritórios e agentes em todo o mundo, na Harbor Lineworks oferecemos soluções integradas de importação e exportação de acordo com as necessidades dos nossos clientes a nível nacional e internacional. Conheça todos os serviços que oferecemos para sua empresa!</p>
<div class="btn about-cta abs">ABOUT US</div>

<div class="service-photo photo-house abs" role="img" aria-label="Two-storey suburban house with freshly painted grey exterior"></div>
<div class="service-block residential abs">
  <h2 class="service-title">Residential<br>Painting</h2>
  <p class="service-lead">Does your home need life brought back into it?</p>
  <ul class="service-list">
    <li><svg width="44" height="20" viewBox="0 0 44 20"><path d="M2 7h26V1l14 9-14 9v-6H2z" fill="#8a0a1f"/></svg>Interior house painting</li>
    <li><svg width="44" height="20" viewBox="0 0 44 20"><path d="M2 7h26V1l14 9-14 9v-6H2z" fill="#8a0a1f"/></svg>Exterior home painting</li>
    <li><svg width="44" height="20" viewBox="0 0 44 20"><path d="M2 7h26V1l14 9-14 9v-6H2z" fill="#8a0a1f"/></svg>Cabinet painting</li>
    <li><svg width="44" height="20" viewBox="0 0 44 20"><path d="M2 7h26V1l14 9-14 9v-6H2z" fill="#8a0a1f"/></svg>Deck &amp; fence painting</li>
    <li><svg width="44" height="20" viewBox="0 0 44 20"><path d="M2 7h26V1l14 9-14 9v-6H2z" fill="#8a0a1f"/></svg>Drywall repair</li>
  </ul>
</div>

<div class="service-block commercial abs">
  <h2 class="service-title">Commercial<br>Painting</h2>
  <p class="service-lead">Does your home need life brought back into it?</p>
  <ul class="service-list">
    <li><svg width="44" height="20" viewBox="0 0 44 20"><path d="M2 7h26V1l14 9-14 9v-6H2z" fill="#8a0a1f"/></svg>Medical Facilities</li>
    <li><svg width="44" height="20" viewBox="0 0 44 20"><path d="M2 7h26V1l14 9-14 9v-6H2z" fill="#8a0a1f"/></svg>Education centers</li>
    <li><svg width="44" height="20" viewBox="0 0 44 20"><path d="M2 7h26V1l14 9-14 9v-6H2z" fill="#8a0a1f"/></svg>Gyms and fitness centers</li>
    <li><svg width="44" height="20" viewBox="0 0 44 20"><path d="M2 7h26V1l14 9-14 9v-6H2z" fill="#8a0a1f"/></svg>Religious institutions</li>
    <li><svg width="44" height="20" viewBox="0 0 44 20"><path d="M2 7h26V1l14 9-14 9v-6H2z" fill="#8a0a1f"/></svg>Property management</li>
  </ul>
</div>
<div class="photo-building abs" role="img" aria-label="Commercial building with blue metal siding and roll-up doors"></div>

<section class="reviews abs"></section>
<h2 class="section-title reviews-title abs">Reviews</h2>
<div class="review review-1 abs">
  <div class="stars">
    <svg width="42" height="40" viewBox="0 0 24 23"><path d="M12 0l2.9 8.3H24l-7.3 5.4 2.8 8.8L12 17.2l-7.5 5.3 2.8-8.8L0 8.3h9.1z" fill="#a50f2a"/></svg>
    <svg width="42" height="40" viewBox="0 0 24 23"><path d="M12 0l2.9 8.3H24l-7.3 5.4 2.8 8.8L12 17.2l-7.5 5.3 2.8-8.8L0 8.3h9.1z" fill="#a50f2a"/></svg>
    <svg width="42" height="40" viewBox="0 0 24 23"><path d="M12 0l2.9 8.3H24l-7.3 5.4 2.8 8.8L12 17.2l-7.5 5.3 2.8-8.8L0 8.3h9.1z" fill="#a50f2a"/></svg>
    <svg width="42" height="40" viewBox="0 0 24 23"><path d="M12 0l2.9 8.3H24l-7.3 5.4 2.8 8.8L12 17.2l-7.5 5.3 2.8-8.8L0 8.3h9.1z" fill="#a50f2a"/></svg>
    <svg width="42" height="40" viewBox="0 0 24 23"><path d="M12 0l2.9 8.3H24l-7.3 5.4 2.8 8.8L12 17.2l-7.5 5.3 2.8-8.8L0 8.3h9.1z" fill="#a50f2a"/></svg>
  </div>
  <p class="review-text">Interdum et malesuada fames ac ante<br>&nbsp;ipsum primis in faucibus donec<br>&nbsp;tempor nisi neque.</p>
  <p class="review-name">Dana Whitlock</p>
</div>
<div class="review review-2 abs">
  <div class="stars">
    <svg width="42" height="40" viewBox="0 0 24 23"><path d="M12 0l2.9 8.3H24l-7.3 5.4 2.8 8.8L12 17.2l-7.5 5.3 2.8-8.8L0 8.3h9.1z" fill="#a50f2a"/></svg>
    <svg width="42" height="40" viewBox="0 0 24 23"><path d="M12 0l2.9 8.3H24l-7.3 5.4 2.8 8.8L12 17.2l-7.5 5.3 2.8-8.8L0 8.3h9.1z" fill="#a50f2a"/></svg>
    <svg width="42" height="40" viewBox="0 0 24 23"><path d="M12 0l2.9 8.3H24l-7.3 5.4 2.8 8.8L12 17.2l-7.5 5.3 2.8-8.8L0 8.3h9.1z" fill="#a50f2a"/></svg>
    <svg width="42" height="40" viewBox="0 0 24 23"><path d="M12 0l2.9 8.3H24l-7.3 5.4 2.8 8.8L12 17.2l-7.5 5.3 2.8-8.8L0 8.3h9.1z" fill="#a50f2a"/></svg>
    <svg width="42" height="40" viewBox="0 0 24 23"><path d="M12 0l2.9 8.3H24l-7.3 5.4 2.8 8.8L12 17.2l-7.5 5.3 2.8-8.8L0 8.3h9.1z" fill="#a50f2a"/></svg>
  </div>
  <p class="review-text">Interdum et malesuada fames ac ante<br>&nbsp;ipsum primis in faucibus donec<br>&nbsp;tempor nisi neque.</p>
  <p class="review-name">Dana Whitlock</p>
</div>

<h2 class="section-title results-title abs">Our Results</h2>
<div class="slider-arrow abs" style="left:58px">&#8249;</div>
<div class="result result-1 abs" role="img" aria-label="Modern house entrance with wood slat fence and lanterns"></div>
<div class="result result-2 abs" role="img" aria-label="White courtyard walkway with blue trim and lanterns"></div>
<div class="result result-3 abs" role="img" aria-label="Freshly painted hallway with staircase and wood floor"></div>
<div class="slider-arrow abs" style="left:1106px">&#8250;</div>

<section class="quote abs"></section>
<h2 class="section-title quote-title abs">Get A Quote</h2>
<div class="field abs" style="left:269px;top:3383px;width:316px;height:38px">Your Name</div>
<div class="field abs" style="left:620px;top:3383px;width:315px;height:38px">Your Phone</div>
<div class="field abs" style="left:269px;top:3450px;width:316px;height:38px">Email Address</div>
<div class="field abs" style="left:620px;top:3450px;width:315px;height:38px">Select Service</div>
<div class="field abs" style="left:269px;top:3512px;width:666px;height:84px">Additional Message</div>
<div class="quote-submit abs">GET A FREE QUOTE NOW</div>

<footer class="site-footer abs"></footer>
<div class="footer-brand abs"><span class="brand-mark"></span>BRUSHWELL CRAFTS</div>
<p class="footer-about abs">Lorem ipsum dolor sit amet, consectetur adipiscing elit, sed do eiusmod temporincididunt ut labore et doloremagna aliqua.</p>
<div class="socials abs"><span class="social-dot"></span><span class="social-dot"></span><span class="social-dot"></span></div>

<div class="quick-links abs">
  <h3 class="footer-heading">QUICK LINKS</h3>
  <ul><li>Home</li><li>About</li><li>Services</li><li>Projects</li></ul>
</div>

<div class="contact-info abs">
  <h3 class="footer-heading">CONTACT INFO</h3>
  <div class="contact-row">
    <span class="contact-icon"><svg width="12" height="12" viewBox="0 0 24 24"><path d="M6.6 10.8a15 15 0 0 0 6.6 6.6l2.2-2.2a1 1 0 0 1 1-.25 11.4 11.4 0 0 0 3.6.57 1 1 0 0 1 1 1V20a1 1 0 0 1-1 1A17 17 0 0 1 3 4a1 1 0 0 1 1-1h3.5a1 1 0 0 1 1 1c0 1.25.2 2.45.57 3.57a1 1 0 0 1-.25 1z" fill="#fff"/></svg></span>
    <div><div class="contact-label">CALL US</div><div class="contact-value">555 014 7731</div></div>
  </div>
  <div class="contact-row">
    <span class="contact-icon"><svg width="12" height="10" viewBox="0 0 12 10"><rect x="0" y="0" width="12" height="10" rx="1" fill="#fff"/><path d="M0.5 1l5.5 4 5.5-4" stroke="#8a0a1f" stroke-width="1.2" fill="none"/></svg></span>
    <div><div class="contact-label">SEND AN EMAIL</div><div class="contact-value">hello@brushwellcrafts.com</div></div>
  </div>
  <div class="contact-row">
    <span class="contact-icon"><svg width="10" height="13" viewBox="0 0 10 13"><path d="M5 0a5 5 0 0 1 5 5c0 3.5-5 8-5 8S0 8.5 0 5a5 5 0 0 1 5-5z" fill="#fff"/><circle cx="5" cy="5" r="1.8" fill="#8a0a1f"/></svg></span>
    <div><div class="contact-label">LOCATION</div><div class="contact-value">Your Address Here</div></div>
  </div>
</div>

<div class="stay-updated abs">
  <h3 class="footer-heading">STAY UPDATED</h3>
  <div class="newsletter-input">EMAIL ADDRESS</div>
  <div class="newsletter-btn">SIGNUP NOW</div>
</div>

<p class="copyright abs">Copyright 2024 Brushwell Crafts. All Rights Reserved.</p>
<p class="legal abs">Privacy Policy | Terms &amp; Conditions</p>

</body>
</html>
```